Graphic design for "How It Works" for VelmoraStyles.com*

VelmoraStyles.com website is for selling custom designer outfits for women and girls in all countries, customers can choose existing designs on this website and customize to their measurements. Customers can also provide their own designs and measurements and our expert designers and tailors get the outfit stitched and delivered to the customer.

We wanted to explain how this entire process works in 4 steps in the form of graphic design with little heading and text describing each step.

Step 1: Select Dress
Its time to choose the beauty you want to adorn yourself with. We have a wide collection of premium dresses, colours and accessories. There is something for everyone! All you need to do is pick. If you can’t find what you are looking for then you can share a picture of what you want, we will get it done whatever you want.

Step 2: Customization
Everyone is different; hence we realise the need for customization of the design and size. Here you select exactly how you want your dress to be. From sleeves to cuts, everything will be done as per your wish. Enter your measurements, lo and behold! You’re done. Leave your comments for even more customization.

Step 3: Designer Consultation
We as a user-friendly brand, aspire to provide the best of services to our clients. Our expert lady designers will help you for everything right from selecting of fabric to design of dress to necessary accessories. Our designers are just a call away!

Step 4: Stitch and Deliver
After you have placed your order, we confirm and verify the details. The boutique completes your order, sends it to us and we deliver it to your doorstep. We also have a team of designers in-house to cater to your premium dressing needs.

```html
<!DOCTYPE html>
<html lang="en">
<head>
<meta charset="UTF-8">
<title>How it works – VelmoraStyles.com</title>
<link href="https://fonts.googleapis.com/css2?family=Lato:wght@400&family=Oswald:wght@600&display=swap" rel="stylesheet">
<style>
  :root {
    --title-pink: #e0305f;
    --step-red: #f04e37;
    --step-teal: #45949a;
    --step-blue: #2479c0;
    --step-purple: #8a3a7a;
    --body-text: #2b2b2b;
    --divider: #9a9a9a;
    --icon-tone: #d9d9d9;
    --page-bg: #ffffff;
  }
  html, body {
    margin: 0;
    padding: 0;
    overflow: hidden;
    background: var(--page-bg);
  }
  .how-it-works {
    position: relative;
    width: 1200px;
    height: 370px;
    overflow: hidden;
    background: var(--page-bg);
  }
  .section-title {
    position: absolute;
    top: 2px;
    left: 0;
    width: 100%;
    margin: 0;
    text-align: center;
    font-family: "Lato", sans-serif;
    font-weight: 400;
    font-size: 38px;
    line-height: 44px;
    color: var(--title-pink);
    letter-spacing: -0.3px;
  }
  .step-badge {
    position: absolute;
    top: 48px;
    width: 170px;
    height: 180px;
  }
  .step-badge svg {
    position: absolute;
    inset: 0;
  }
  .step-label {
    position: absolute;
    left: 0;
    width: 170px;
    text-align: center;
    font-family: "Oswald", sans-serif;
    font-weight: 600;
    font-size: 21px;
    line-height: 22px;
    color: #fff;
    letter-spacing: 0.3px;
    margin: 0;
  }
  .step-label.two-line { top: 96px; }
  .step-label.one-line { top: 97px; }
  .step-text {
    position: absolute;
    top: 229px;
    width: 282px;
    margin: 0;
    text-align: center;
    font-family: "Lato", sans-serif;
    font-size: 12.6px;
    line-height: 16px;
    color: var(--body-text);
  }
  .column-divider {
    position: absolute;
    top: 222px;
    height: 135px;
    border-left: 1px dotted var(--divider);
  }
</style>
</head>
<body>
<main class="how-it-works">
  <h1 class="section-title">How it works</h1>

  <svg width="0" height="0" style="position:absolute">
    <defs>
      <clipPath id="badge-clip"><circle cx="85" cy="85" r="77"/></clipPath>
      <filter id="badge-shadow" x="-50%" y="-200%" width="200%" height="500%">
        <feGaussianBlur stdDeviation="5"/>
      </filter>
    </defs>
  </svg>

  <!-- Step 1 -->
  <div class="step-badge" style="left:65px">
    <svg width="170" height="180" viewBox="0 0 170 180">
      <ellipse cx="85" cy="165" rx="55" ry="6" fill="#000" opacity="0.22" filter="url(#badge-shadow)"/>
      <circle cx="85" cy="85" r="77" fill="#fff"/>
      <rect x="0" y="89" width="170" height="90" fill="var(--step-red)" clip-path="url(#badge-clip)"/>
      <circle cx="85" cy="85" r="77" fill="none" stroke="var(--step-red)" stroke-width="2.5"/>
      <g role="img" aria-label="Dress icon with checklist">
        <rect x="45" y="20" width="80" height="60" rx="6" fill="var(--icon-tone)"/>
      </g>
    </svg>
    <p class="step-label two-line">Select<br>Dress</p>
  </div>
  <p class="step-text" style="left:9px">Its time to choose the beauty you want to adorn yourself with. We have a wide collection of premium dresses, colours and accessories. There is something for everyone! All you need to do is pick. If you can’t find what you are looking for then you can share a picture of what you want, we will get it done whatever you want.</p>

  <div class="column-divider" style="left:294px"></div>

  <!-- Step 2 -->
  <div class="step-badge" style="left:360px">
    <svg width="170" height="180" viewBox="0 0 170 180">
      <ellipse cx="85" cy="165" rx="55" ry="6" fill="#000" opacity="0.22" filter="url(#badge-shadow)"/>
      <circle cx="85" cy="85" r="77" fill="#fff"/>
      <rect x="0" y="89" width="170" height="90" fill="var(--step-teal)" clip-path="url(#badge-clip)"/>
      <circle cx="85" cy="85" r="77" fill="none" stroke="var(--step-teal)" stroke-width="2.5"/>
      <g role="img" aria-label="Tailoring scissors icon">
        <rect x="32" y="30" width="108" height="40" rx="6" fill="var(--icon-tone)"/>
      </g>
    </svg>
    <p class="step-label one-line">Customization</p>
  </div>
  <p class="step-text" style="left:304px">Everyone is different; hence we realise the need for customization of the design and size. Here you select exactly how you want your dress to be. From sleeves to cuts, everything will be done as per your wish. Enter your measurements, lo and behold! You’re done. Leave your comments for even more customization.</p>

  <div class="column-divider" style="left:596px"></div>

  <!-- Step 3 -->
  <div class="step-badge" style="left:663px">
    <svg width="170" height="180" viewBox="0 0 170 180">
      <ellipse cx="85" cy="165" rx="55" ry="6" fill="#000" opacity="0.22" filter="url(#badge-shadow)"/>
      <circle cx="85" cy="85" r="77" fill="#fff"/>
      <rect x="0" y="89" width="170" height="90" fill="var(--step-blue)" clip-path="url(#badge-clip)"/>
      <circle cx="85" cy="85" r="77" fill="none" stroke="var(--step-blue)" stroke-width="2.5"/>
      <g role="img" aria-label="Support headset icon">
        <rect x="48" y="20" width="74" height="62" rx="6" fill="var(--icon-tone)"/>
      </g>
    </svg>
    <p class="step-label two-line">Designer<br>Consultation</p>
  </div>
  <p class="step-text" style="left:607px">We as a user-friendly brand, aspire to provide the best of services to our clients. Our expert lady designers will help you for everything right from selecting of fabric to design of dress to necessary accessories. Our designers are just a call away!</p>

  <div class="column-divider" style="left:898px"></div>

  <!-- Step 4 -->
  <div class="step-badge" style="left:965px">
    <svg width="170" height="180" viewBox="0 0 170 180">
      <ellipse cx="85" cy="165" rx="55" ry="6" fill="#000" opacity="0.22" filter="url(#badge-shadow)"/>
      <circle cx="85" cy="85" r="77" fill="#fff"/>
      <rect x="0" y="89" width="170" height="90" fill="var(--step-purple)" clip-path="url(#badge-clip)"/>
      <circle cx="85" cy="85" r="77" fill="none" stroke="var(--step-purple)" stroke-width="2.5"/>
      <g role="img" aria-label="Sewing machine and delivery parcel icon">
        <rect x="28" y="20" width="114" height="62" rx="6" fill="var(--icon-tone)"/>
      </g>
    </svg>
    <p class="step-label two-line">Stitch and<br>Deliver</p>
  </div>
  <p class="step-text" style="left:909px">After you have placed your order, we confirm and verify the details. The boutique completes your order, sends it to us and we deliver it to your doorstep. We also have a team of designers in-house to cater to your premium dressing needs.</p>
</main>
</body>
</html>
```